private relaxation massage therapist business card

I want a card that does not give a physical address as I am able to massage at home as well as be mobile. I want on the back somewhere to put appointment details and also my bank acct details for payment being to acct 38 6042 0071846 00
I have a Certificate in Relaxation Massage from KTRB 2014
I would like to use blue colours and maybe have some fluffy clouds somewhere on the business card.

Industry/Entity Type

Massage

Contact Information for Business Card

Megan Pollard
Relaxation Massage Therapist

telephone 0218 647 092 or 09 8416375
email meganpollard72@quillmail.com

Requirements
Must have
• bold lettering, lots of white space, On the reverse of the card some lines in a box for me to write appointment times also on reverse my bank acct details for payment on line.

```html
<!DOCTYPE html>
<html lang="en">
<head>
<meta charset="utf-8">
<title>Megan Pollard – Relaxation Massage Therapist Business Card</title>
<link rel="stylesheet" href="https://fonts.googleapis.com/css2?family=Luckiest+Guy&family=Jost:wght@500;700&display=swap">
<style>
  :root {
    --page: #e9ecee;
    --stripe-light: #d4eef4;
    --stripe-teal: #7fcfdc;
    --teal-deep: #2bb3b0;
    --title-red: #b5475a;
    --photo-warm: #e9d2bd;
    --photo-soft: #c9a692;
    --dash-rose: #c7757a;
    --ink: #1d1d1d;
    --white: #ffffff;
  }
  * { box-sizing: border-box; margin: 0; padding: 0; }
  html, body { width: 1000px; height: 1200px; overflow: hidden; background: var(--page); }
  .canvas { position: relative; width: 1000px; height: 1200px; }
  .card {
    position: absolute; left: 60px; width: 880px; height: 503px; overflow: hidden;
    background: repeating-linear-gradient(90deg, var(--stripe-light) 0 70px, var(--stripe-teal) 70px 140px);
    box-shadow: 0 6px 18px rgba(0,0,0,.18);
  }
  .card--front { top: 60px; }
  .card--back { top: 640px; }
  .card__art { position: absolute; inset: 0; width: 100%; height: 100%; }
  .front__title {
    position: absolute; top: 34px; left: 0; right: 0; text-align: center;
    font-family: "Luckiest Guy", cursive; font-size: 40px; letter-spacing: 1px;
    color: var(--title-red);
  }
  .front__contact {
    position: absolute; top: 212px; left: 330px; width: 320px; text-align: center;
    font-family: "Jost", sans-serif; font-weight: 500; color: var(--ink);
    font-size: 24px; line-height: 1.3;
  }
  .front__name { font-weight: 700; font-size: 32px; }
  .front__features {
    position: absolute; top: 400px; left: 170px; list-style: none;
    font-family: "Jost", sans-serif; font-weight: 700; font-size: 22px; color: var(--ink); line-height: 1.55;
  }
  .front__features li { position: relative; padding-left: 34px; }
  .front__features li::before {
    content: ""; position: absolute; left: 0; top: 11px; width: 16px; height: 10px;
    border-radius: 50%; background: var(--teal-deep);
  }
  .back__payment {
    position: absolute; left: 230px; top: 395px;
    font-family: "Jost", sans-serif; font-weight: 700; font-size: 20px; color: var(--ink);
  }
</style>
</head>
<body>
<main class="canvas">

  <section class="card card--front" aria-label="Business card front">
    <svg class="card__art" viewBox="0 0 880 503" aria-hidden="false">
      <defs>
        <linearGradient id="photoTone" x1="0" y1="0" x2="1" y2="1">
          <stop offset="0" stop-color="var(--photo-warm)"/>
          <stop offset="1" stop-color="var(--photo-soft)"/>
        </linearGradient>
      </defs>
      <path class="front__cloud-band" fill="var(--teal-deep)"
        d="M0,340 C60,280 160,250 230,280 C260,180 380,130 480,140 C580,150 650,190 670,230 C720,190 820,180 880,220 L880,503 L0,503 Z"/>
      <path class="front__photo" role="img" aria-label="Photo of a client lying face down receiving a relaxing back massage"
        fill="url(#photoTone)"
        d="M0,362 C60,302 160,272 230,302 C260,202 380,152 480,162 C580,172 650,212 670,252 C720,212 820,202 880,242 L880,503 L0,503 Z"/>
      <path class="front__stitch" fill="none" stroke="var(--dash-rose)" stroke-width="3" stroke-dasharray="12 8"
        d="M10,392 C70,332 170,302 245,332 C275,232 385,182 480,192 C575,202 640,242 660,282 L672,282 C725,242 820,235 870,270"/>
    </svg>
    <h1 class="front__title">Megan Pollard Relaxation Massage Therapist</h1>
    <div class="front__contact">
      <p class="front__name">Megan Pollard</p>
      <p>0218 647 092</p>
      <p>09 841 6375</p>
      <p>meganpollard72@quillmail.com</p>
    </div>
    <ul class="front__features">
      <li>Able massage at home as well as be mobile</li>
      <li>Certificate in Relaxation Massage from KTRB 2014</li>
    </ul>
  </section>

  <section class="card card--back" aria-label="Business card back">
    <svg class="card__art" viewBox="0 0 880 503">
      <path class="back__cloud" fill="var(--white)" stroke="var(--teal-deep)" stroke-width="12"
        d="M170,150 C170,90 260,70 320,95 C360,45 480,40 530,85 C590,45 720,60 730,130 C800,140 820,230 770,270 C820,320 790,420 700,415 C660,460 540,460 500,425 C440,465 320,460 290,420 C200,440 130,390 160,330 C100,300 100,190 170,150 Z"/>
      <g class="back__write-lines" stroke="var(--teal-deep)" stroke-width="2" stroke-dasharray="8 7">
        <line x1="200" y1="145" x2="700" y2="145"/>
        <line x1="180" y1="210" x2="740" y2="210"/>
        <line x1="180" y1="275" x2="740" y2="275"/>
        <line x1="190" y1="340" x2="730" y2="340"/>
        <line x1="230" y1="425" x2="690" y2="425"/>
      </g>
    </svg>
    <p class="back__payment">Payment being to acct: 38 6042 0071846 00</p>
  </section>

</main>
</body>
</html>
```